Payday Lending App Interface Design

Hello, we are building a payday lending application, Lendoro, that lend people money. I have drafted some of the screens that show the functionalities we have at the moment, please find the screens in attachments.
The elements in the screens are placed just to show what should be included in those screens, it's not necessary to follow the same layout. If you have better design ideas, you are very welcomed to show off your talent.
I think what we want is a style guide so that we can apply the same style to any screens that are similar to the ones I attached. We really like
the style as in the attached image called Style.png. We might want something similar - a simple, clean design yet fun and engaging. Customised graphical elements such as icons, illustrations are preferable.
Apart from the attached screens, we might also need a design for the On Board screen and the Login/Sign Up screen too.
Our logo colour is in yellow and black. Perhaps we will have a similar colour theme. I also attached the logo file, icon-Lendoro.png, if you would like to put it in your design.
Please message me if you need further information.
Regards
Target Market(s)
Young people that doesn't have strong income
Look and feel
Each slider illustrates characteristics of the customer's brand and the style your logo design should communicate.

```html
<!DOCTYPE html>
<html lang="en">
<head>
<meta charset="utf-8">
<title>Lendoro – App Screens</title>
<link href="https://fonts.googleapis.com/css2?family=Montserrat:wght@400;500;600;700&display=swap" rel="stylesheet">
<style>
  :root {
    --brand-yellow: #f9d40e;
    --brand-yellow-deep: #e8c200;
    --ink: #111111;
    --text: #1d1d1d;
    --muted: #8a8a8a;
    --faint: #c4c4c4;
    --line: #e3e3e3;
    --ok-green: #8dd15a;
    --ok-border: #b9e29a;
    --alert-red: #f04c24;
    --alert-border: #f2826a;
    --disabled: #d4d4d4;
    --stage: #f1f1ee;
    --white: #ffffff;
    --overlay: #8c8c8c;
  }
  * { box-sizing: border-box; margin: 0; padding: 0; }
  html, body { width: 1200px; height: 666px; overflow: hidden; }
  body { font-family: "Montserrat", sans-serif; color: var(--text); background: var(--stage); }
  .canvas { position: relative; width: 1200px; height: 666px; overflow: hidden; background: var(--stage); }

  .screen { position: absolute; background: var(--white); overflow: hidden; box-shadow: 0 6px 24px rgba(0,0,0,0.08); }

  /* ---------- Personal details ---------- */
  .details { left: 127px; top: 141px; width: 218px; height: 430px; }
  .details .back { position: absolute; left: 14px; top: 25px; width: 10px; height: 12px; }
  .details .title { position: absolute; left: 0; right: 0; top: 24px; text-align: center; font-size: 14.5px; font-weight: 700; }
  .details .subtitle { position: absolute; left: 40px; right: 40px; top: 48px; text-align: center; font-size: 9px; line-height: 12px; font-weight: 500; }
  .field { position: absolute; left: 15px; width: 189px; height: 32px; border: 1px solid var(--line); border-radius: 6px; box-shadow: 0 2px 5px rgba(0,0,0,0.08); display: flex; align-items: center; padding-left: 8px; gap: 6px; font-size: 7.5px; color: var(--muted); font-weight: 500; }
  .field svg { width: 9px; height: 10px; flex: none; }
  .field.date { font-size: 9px; letter-spacing: 0.5px; }
  .btn-next { position: absolute; left: 15px; top: 361px; width: 189px; height: 32px; border-radius: 6px; background: var(--brand-yellow); display: flex; align-items: center; justify-content: center; font-size: 11.5px; font-weight: 700; color: var(--ink); }

  /* ---------- Dashboard ---------- */
  .dashboard { left: 393px; top: 118px; width: 215px; height: 478px; border-radius: 18px; background: #fbfbfb; }
  .status { position: absolute; left: 16px; top: 9px; font-size: 8px; font-weight: 600; }
  .status-icons { position: absolute; right: 14px; top: 10px; width: 22px; height: 7px; }
  .dashboard .menu-icon { position: absolute; left: 7px; top: 37px; width: 15px; height: 12px; }
  .dashboard .greeting { position: absolute; left: 0; right: 0; top: 33px; text-align: center; font-size: 17px; font-weight: 700; }
  .dashboard .gear { position: absolute; right: 9px; top: 35px; width: 17px; height: 17px; }
  .step { position: absolute; left: 21px; width: 173px; background: var(--white); border: 1px solid var(--line); border-radius: 6px; padding: 0 10px 0 24px; font-size: 8.5px; font-weight: 600; }
  .step::before { content: ""; position: absolute; left: 10px; top: 12px; width: 5px; height: 5px; border-radius: 50%; background: var(--disabled); }
  .step.short { height: 29px; line-height: 27px; }
  .step.done { border-color: var(--ok-border); }
  .step.done::before { background: var(--ok-green); }
  .step.alert { border-color: var(--alert-border); padding-top: 8px; }
  .step.alert::before { background: var(--alert-red); top: 13px; }
  .step.active { padding-top: 8px; }
  .step.active::before { background: var(--ok-green); top: 13px; }
  .step.locked { color: var(--faint); }
  .step .step-title { line-height: 11px; }
  .step .step-note { font-size: 7px; font-weight: 500; color: #555; line-height: 10px; margin-top: 3px; }
  .step .step-btn { position: absolute; left: 7px; right: 7px; height: 26px; border-radius: 5px; display: flex; align-items: center; padding-left: 12px; font-size: 7.5px; font-weight: 600; color: var(--white); }
  .step-btn.red { background: var(--alert-red); bottom: 12px; box-shadow: 0 2px 4px rgba(240,76,36,0.3); }
  .step-btn.grey { background: var(--disabled); bottom: 12px; }

  /* ---------- Bank connection ---------- */
  .connecting { left: 656px; top: 141px; width: 218px; height: 430px; }
  .brand-tile { position: absolute; left: 63px; top: 38px; width: 92px; height: 92px; border-radius: 16px; background: var(--brand-yellow); display: flex; align-items: center; justify-content: center; font-size: 15px; font-weight: 700; color: var(--ink); }
  .spinner { position: absolute; left: 95px; top: 188px; width: 30px; height: 30px; }
  .connecting .heading { position: absolute; left: 0; right: 0; top: 271px; text-align: center; font-size: 17px; line-height: 20px; font-weight: 700; }
  .connecting .body { position: absolute; left: 30px; right: 30px; top: 322px; text-align: center; font-size: 10px; line-height: 16px; font-weight: 500; }

  /* ---------- Side menu ---------- */
  .side-menu { left: 921px; top: 141px; width: 218px; height: 430px; background: var(--overlay); }
  .overlay-card { position: absolute; left: 170px; width: 40px; border: 1px solid #a5a5a5; border-radius: 6px; }
  .overlay-gear { position: absolute; right: 6px; top: 21px; width: 16px; height: 16px; }
  .drawer { position: absolute; left: 0; top: 0; width: 174px; height: 430px; background: var(--brand-yellow); overflow: hidden; }
  .drawer-curve { position: absolute; background: var(--brand-yellow-deep); border-radius: 50%; }
  .drawer .close { position: absolute; left: 16px; top: 20px; width: 11px; height: 11px; }
  .avatar { position: absolute; left: 62px; top: 9px; width: 48px; height: 48px; border-radius: 50%; border: 2px solid var(--white); background: radial-gradient(circle at 50% 40%, #c7b6a6, #5d4c42); }
  .drawer .name { position: absolute; left: 0; right: 0; top: 68px; text-align: center; font-size: 13px; font-weight: 700; }
  .drawer .handle { position: absolute; left: 0; right: 0; top: 87px; text-align: center; font-size: 9px; font-weight: 500; }
  .menu-link { position: absolute; left: 12px; width: 150px; height: 27px; background: var(--ink); color: var(--white); font-size: 9.5px; font-weight: 600; display: flex; align-items: center; justify-content: space-between; padding: 0 6px; border-radius: 1px; }
  .menu-link svg { width: 5px; height: 8px; }
  .app-mark { position: absolute; left: 41px; top: 392px; display: flex; align-items: center; gap: 6px; font-size: 7.5px; font-weight: 500; }
  .app-mark .square { width: 26px; height: 26px; background: var(--white); border-radius: 3px; }
</style>
</head>
<body>
<main class="canvas">

  <!-- Personal details -->
  <section class="screen details">
    <svg class="back" viewBox="0 0 10 12"><path d="M7 1 L2 6 L7 11" fill="none" stroke="#111" stroke-width="1.6"/></svg>
    <h1 class="title">Personal Details</h1>
    <p class="subtitle">Please provide details as shown on ID</p>
    <div class="field" style="top:127px"><svg viewBox="0 0 9 10"><circle cx="4.5" cy="3" r="2.2" fill="none" stroke="#f9d40e" stroke-width="1"/><path d="M0.8 9.5 C1 6 8 6 8.2 9.5" fill="none" stroke="#f9d40e" stroke-width="1"/></svg>Given Name</div>
    <div class="field" style="top:176px"><svg viewBox="0 0 9 10"><circle cx="4.5" cy="3" r="2.2" fill="none" stroke="#f9d40e" stroke-width="1"/><path d="M0.8 9.5 C1 6 8 6 8.2 9.5" fill="none" stroke="#f9d40e" stroke-width="1"/></svg>Middle Name</div>
    <div class="field" style="top:224px"><svg viewBox="0 0 9 10"><circle cx="4.5" cy="3" r="2.2" fill="none" stroke="#f9d40e" stroke-width="1"/><path d="M0.8 9.5 C1 6 8 6 8.2 9.5" fill="none" stroke="#f9d40e" stroke-width="1"/></svg>Sirname</div>
    <div class="field date" style="top:273px"><svg viewBox="0 0 9 10"><rect x="0.5" y="1.5" width="8" height="8" rx="1" fill="none" stroke="#f9d40e"/><path d="M0.5 4 H8.5" stroke="#f9d40e"/></svg>_ _ / _ _ / 20_ _</div>
    <div class="btn-next">NEXT</div>
  </section>

  <!-- Dashboard -->
  <section class="screen dashboard">
    <span class="status">9:41</span>
    <svg class="status-icons" viewBox="0 0 22 7"><path d="M1 3 Q4 0 7 3 M2.5 4.5 Q4 3 5.5 4.5" fill="none" stroke="#111" stroke-width="0.9"/><rect x="10" y="1" width="10" height="5" rx="1" fill="none" stroke="#111" stroke-width="0.8"/><rect x="11" y="2" width="7" height="3" fill="#111"/></svg>
    <svg class="menu-icon" viewBox="0 0 15 12"><path d="M0 1 H15 M0 6 H11 M0 11 H7" stroke="#111" stroke-width="1.4"/></svg>
    <h1 class="greeting">Hi, Username</h1>
    <svg class="gear" viewBox="0 0 24 24"><path d="M12 2 l2 0 .6 2.7 2 .9 2.4-1.5 1.5 1.5-1.5 2.4.9 2 2.7.6v2l-2.7.6-.9 2 1.5 2.4-1.5 1.5-2.4-1.5-2 .9L14 22h-2h-2l-.6-2.7-2-.9-2.4 1.5-1.5-1.5 1.5-2.4-.9-2L1.4 13v-2l2.7-.6.9-2-1.5-2.4 1.5-1.5 2.4 1.5 2-.9L10 2z" fill="none" stroke="#111" stroke-width="1.4"/><circle cx="12" cy="12" r="3.5" fill="none" stroke="#111" stroke-width="1.4"/></svg>

    <div class="step short done" style="top:75px">Start</div>
    <div class="step alert" style="top:114px;height:124px">
      <div class="step-title">Upload Your Personal Information</div>
      <div class="step-note">It seems like your ID documents are expire. Upload your document again to get qualified</div>
      <div class="step-btn red">Upload and Qualify My IDs</div>
    </div>
    <div class="step short done" style="top:248px">Connect Bank account</div>
    <div class="step active" style="top:286px;height:83px">
      <div class="step-title">Apply a Load</div>
      <div class="step-note">Get Your loan that fit to your need</div>
      <div class="step-btn grey">Apply Now</div>
    </div>
    <div class="step short locked" style="top:378px">Repayments</div>
    <div class="step short locked" style="top:416px">Loan Closed</div>
  </section>

  <!-- Bank connection -->
  <section class="screen connecting">
    <div class="brand-tile">Lendoro</div>
    <svg class="spinner" viewBox="0 0 30 30">
      <circle cx="15" cy="4" r="2.6" fill="#111"/>
      <circle cx="22.8" cy="7.2" r="2.6" fill="#2a2a2a"/>
      <circle cx="26" cy="15" r="2.6" fill="#444"/>
      <circle cx="22.8" cy="22.8" r="2.6" fill="#666"/>
      <circle cx="15" cy="26" r="2.6" fill="#888"/>
      <circle cx="7.2" cy="22.8" r="2.6" fill="#a8a8a8"/>
      <circle cx="4" cy="15" r="2.6" fill="#c4c4c4"/>
      <circle cx="7.2" cy="7.2" r="2.6" fill="#dcdcdc"/>
    </svg>
    <h1 class="heading">Connecting to<br>your bank...</h1>
    <p class="body">Please don’t exit the app. it takes 3-5 minutes to confirm your etails with your bank</p>
  </section>

  <!-- Side menu -->
  <section class="screen side-menu">
    <div class="overlay-card" style="top:58px;height:28px"></div>
    <div class="overlay-card" style="top:95px;height:120px"></div>
    <div class="overlay-card" style="top:220px;height:28px"></div>
    <div class="overlay-card" style="top:256px;height:82px"></div>
    <div class="overlay-card" style="top:347px;height:28px"></div>
    <div class="overlay-card" style="top:385px;height:28px"></div>
    <svg class="overlay-gear" viewBox="0 0 24 24"><path d="M12 2 l2 0 .6 2.7 2 .9 2.4-1.5 1.5 1.5-1.5 2.4.9 2 2.7.6v2l-2.7.6-.9 2 1.5 2.4-1.5 1.5-2.4-1.5-2 .9L14 22h-2h-2l-.6-2.7-2-.9-2.4 1.5-1.5-1.5 1.5-2.4-.9-2L1.4 13v-2l2.7-.6.9-2-1.5-2.4 1.5-1.5 2.4 1.5 2-.9L10 2z" fill="none" stroke="#111" stroke-width="1.4"/><circle cx="12" cy="12" r="3.5" fill="none" stroke="#111" stroke-width="1.4"/></svg>

    <nav class="drawer">
      <div class="drawer-curve" style="left:120px;top:-60px;width:130px;height:130px"></div>
      <div class="drawer-curve" style="left:-60px;top:360px;width:120px;height:120px"></div>
      <svg class="close" viewBox="0 0 11 11"><path d="M1 1 L10 10 M10 1 L1 10" stroke="#111" stroke-width="1.6"/></svg>
      <div class="avatar" role="img" aria-label="Profile photo of the signed-in user"></div>
      <div class="name">Hi, Username</div>
      <div class="handle">username_00121</div>
      <a class="menu-link" style="top:121px">Loan Products<svg viewBox="0 0 5 8"><path d="M1 1 L4 4 L1 7" fill="none" stroke="#fff"/></svg></a>
      <a class="menu-link" style="top:156px">Loan History<svg viewBox="0 0 5 8"><path d="M1 1 L4 4 L1 7" fill="none" stroke="#fff"/></svg></a>
      <a class="menu-link" style="top:191px">Q &amp; A<svg viewBox="0 0 5 8"><path d="M1 1 L4 4 L1 7" fill="none" stroke="#fff"/></svg></a>
      <a class="menu-link" style="top:290px">Contact Us<svg viewBox="0 0 5 8"><path d="M1 1 L4 4 L1 7" fill="none" stroke="#fff"/></svg></a>
      <a class="menu-link" style="top:329px">Termers &amp; Conditions<svg viewBox="0 0 5 8"><path d="M1 1 L4 4 L1 7" fill="none" stroke="#fff"/></svg></a>
      <div class="app-mark"><span class="square"></span>Lendoro v.1.0</div>
    </nav>
  </section>

</main>
</body>
</html>
```